Handout design project

Hi,

We (shiftlane) provide clients with training on a Point of Sale system called Tallo.

At the end of the training, we want to leave them with a set of quick reference cards. The cards which will be laminated, or printed on glossy card and bound together with a key ring.

The cards will be kept next to the till so users can refer to them if they don't remember how to complete a certain task.
Updates

Target Market(s)

Shop owners and cashiers who are starting to use www.Tallohub.example after they complete our training

Industry/Entity Type

Training

Requirements
Must have
• The design must contain:
- our logo (Shiftlane)
- the Tallo logo
- The card should 'look' Shiftlane (so the primary colours should be ours)

We should be able to modify the contents of the card so that we can create more and more cards with the same look and feel.
So it needs to be done with tools that we have (MS Office, powerpoint, word) or that we can get for free (like GIMP).

In any case, you will need to give instructions on what we should do to make new cards and to edit their contents

There should be a footer at the bottom of each card with:
- the link to the tallo help (see in the attached sample file)
- keywords to search there
- Shiftlane support contact details
Nice to have
• A round mark on the card showing where a hole should be punched in order to go on the keyring.

```html
<!DOCTYPE html>
<html lang="en">
<head>
<meta charset="utf-8">
<title>Tallo quick reference cards – Shiftlane</title>
<link rel="stylesheet" href="https://fonts.googleapis.com/css2?family=Oswald:wght@400;500&family=Roboto:wght@300;400;700&display=swap">
<style>
  :root {
    --orange-deep: #e04a1a;
    --orange: #ea5d24;
    --orange-light: #f38a52;
    --orange-text: #e35a22;
    --green: #3d9b2c;
    --green-light: #6cbf3f;
    --green-text: #3a9a2a;
    --paper: #f6f3ee;
    --ink: #333333;
    --ink-soft: #555555;
    --link: #2a8ac8;
    --rule: #8a8a8a;
    --white: #ffffff;
  }
  * { box-sizing: border-box; margin: 0; padding: 0; }
  html, body { width: 1200px; height: 776px; overflow: hidden; background: var(--paper); }
  body { font-family: "Roboto", Arial, sans-serif; color: var(--ink); position: relative; }

  .backdrop { position: absolute; inset: 0; width: 1200px; height: 776px; }

  .punch-hole { position: absolute; top: 36px; width: 38px; height: 38px; border-radius: 50%; background: var(--white); }
  .punch-hole--left { left: 527px; }
  .punch-hole--right { left: 636px; }

  .brand-name {
    position: absolute; top: 52px;
    font-family: "Roboto", Arial, sans-serif; font-weight: 400;
    font-size: 34px; letter-spacing: 1px; color: var(--white);
  }
  .brand-name--left { left: 36px; }
  .brand-name--right { right: 36px; }

  .card { position: absolute; top: 0; width: 600px; height: 776px; }
  .card--left { left: 0; }
  .card--right { left: 600px; }

  .card-title {
    position: absolute; top: 268px; display: flex; align-items: center; gap: 12px;
  }
  .card--left .card-title { left: 37px; }
  .card--right .card-title { left: 192px; }
  .title-marker {
    width: 58px; height: 58px; flex: none; border-radius: 12px;
    background: var(--orange);
  }
  .title-text {
    font-family: "Oswald", "Arial Narrow", sans-serif; font-weight: 400;
    font-size: 37px; line-height: 1; color: var(--orange-text);
    border-bottom: 4px solid var(--orange-light); padding: 6px 0 8px;
  }

  .steps { position: absolute; top: 352px; list-style: none; font-weight: 300; font-size: 16px; line-height: 21px; }
  .steps li { position: relative; margin-bottom: 8px; }
  .card--left .steps { left: 37px; width: 490px; }
  .card--left .steps li { padding-left: 33px; }
  .card--left .steps li::before { content: "➢"; position: absolute; left: 0; top: 0; font-size: 14px; }
  .card--right .steps { right: 50px; width: 430px; text-align: right; }
  .card--right .steps li { padding-right: 22px; }
  .card--right .steps li::after { content: "◂"; position: absolute; right: 0; top: 0; font-size: 14px; }

  .footer { position: absolute; top: 578px; width: 405px; }
  .card--left .footer { left: 150px; text-align: right; }
  .card--right .footer { left: 37px; text-align: left; }
  .help-link { font-size: 15px; color: var(--link); text-decoration: none; display: block; margin-bottom: 8px; }
  .keywords {
    border-top: 2px solid var(--rule); border-bottom: 2px solid var(--rule);
    padding: 6px 0 4px; font-size: 17px; color: var(--ink-soft); font-weight: 300;
  }
  .keywords strong {
    font-family: "Oswald", "Arial Narrow", sans-serif; font-weight: 500;
    font-size: 26px; color: var(--green-text); vertical-align: -2px;
  }
  .contact { margin-top: 14px; font-size: 15px; line-height: 20px; font-weight: 300; color: var(--ink-soft); }
  .contact b { font-weight: 700; color: var(--orange-text); }

  .partner-name {
    position: absolute; top: 698px;
    font-family: "Roboto", Arial, sans-serif; font-weight: 400;
    font-size: 30px; color: var(--white);
  }
  .card--left .partner-name { left: 37px; }
  .card--right .partner-name { right: 36px; }
</style>
</head>
<body>
  <svg class="backdrop" viewBox="0 0 1200 776" aria-hidden="true">
    <defs>
      <linearGradient id="orangeWash" x1="0" y1="0" x2="0" y2="1">
        <stop offset="0" stop-color="#f07a3f"/>
        <stop offset="1" stop-color="#e04a1a"/>
      </linearGradient>
    </defs>
    <path d="M0,0 H1200 V258 C1100,200 900,255 660,255 C420,255 210,135 0,120 Z" fill="var(--orange-light)"/>
    <path d="M0,0 H1200 V235 C1090,175 890,238 650,238 C410,238 200,128 0,112 Z" fill="url(#orangeWash)"/>
    <path d="M0,0 H1200 V180 C1080,130 880,220 640,220 C400,220 200,110 0,100 Z" fill="var(--orange)" opacity="0.55"/>

    <path d="M0,570 C120,570 235,660 300,776 H0 Z" fill="var(--green-light)"/>
    <path d="M0,586 C110,586 215,670 275,776 H0 Z" fill="var(--green)"/>
    <path d="M1200,570 C1080,570 965,660 900,776 H1200 Z" fill="var(--green-light)"/>
    <path d="M1200,586 C1090,586 985,670 925,776 H1200 Z" fill="var(--green)"/>
  </svg>

  <span class="punch-hole punch-hole--left"></span>
  <span class="punch-hole punch-hole--right"></span>

  <div class="brand-name brand-name--left">Shiftlane</div>
  <div class="brand-name brand-name--right">Shiftlane</div>

  <section class="card card--left">
    <h1 class="card-title">
      <span class="title-marker" aria-hidden="true"></span>
      <span class="title-text">PROCESS A RETURN/REFUND</span>
    </h1>
    <ul class="steps">
      <li>‘Sell’ the product that you wish to return</li>
      <li>Change the quantity to be a negative (so -1 if one item is being returned)</li>
      <li>Click the ‘Notes’ button at the bottom of the screen and enter in any information (such as the original purchase date or receipt number)</li>
      <li>Complete the sale as normal and refund the customer money if appropriate</li>
    </ul>
    <div class="footer">
      <a class="help-link" href="http://support.tallohub.example">http://support.tallohub.example</a>
      <p class="keywords">KEYWORDS TO SEARCH: <strong>REFUND, EXCHANGE</strong></p>
      <p class="contact">For additional support contact<br><b>support@shiftlane.example</b> or call<br>us on <b>0400 555 018</b>, if we can’t answer,<br>we will return your call</p>
    </div>
    <div class="partner-name">tallo</div>
  </section>

  <section class="card card--right">
    <h1 class="card-title">
      <span class="title-marker" aria-hidden="true"></span>
      <span class="title-text">EXCHANGE PRODUCT</span>
    </h1>
    <ul class="steps">
      <li>Sell’ the product that you wish to return</li>
      <li>Change the quantity to be a negative (so -1 if one item is being returned)</li>
      <li>Click the ‘Notes’ button at the bottom of the screen and enter in any information (such as the original purchase date or receipt number)</li>
      <li>Add the new item that the customer is exchanging for</li>
      <li>Complete the sale as normal and refund the customer money if appropriatea</li>
    </ul>
    <div class="footer">
      <a class="help-link" href="http://support.tallohub.example">http://support.tallohub.example</a>
      <p class="keywords">KEYWORDS TO SEARCH: <strong>EXCHANGE</strong></p>
      <p class="contact">For additional support contact<br><b>support@shiftlane.example</b> or call<br>us on <b>0400 555 018</b>, if we can’t answer,<br>we will return your call</p>
    </div>
    <div class="partner-name">tallo</div>
  </section>
</body>
</html>
```